Artist needs a CD Cover Design (Post-Apocalyptic Ambience)

We need a CD Cover Design, for an Album coming out in june.
The songs on the album are the original soundtrack of a Dance Show, that tells the story of a post-apocalyptic world. The whole plot is driven by a Ostra, that contaminated the world and should be healed later on. Main places are "Gild Harbor", a kind of Las Vegas, "Umbral Yard" which is a kind of cemetary, "Slagmere", ruled by the Oil business, "Quarrelin" which is a big mine, and the "Haven Loft" where some humans are protected from the pandemy. The main character is a lonely mute young woman.
So, the name of the Album is "Ostra"!
The name should be written on the Cover, in a certain way up to the artist. The color scheme should be more in darkness than joy, as you could figure it out with the story. It would be great if the design could be greater than just the CD cover, in order to be as well on the other side of the CD cover (page 2, 3 and/or 4 of the digipack)
- The name "Ostra" in the design
- A dark-poetic ambience
- A bigger than one-page design (for other sides of the digipack)

```html
<!DOCTYPE html>
<html lang="en">
<head>
<meta charset="utf-8">
<title>Lucien Marrow — Ostra</title>
<link href="https://fonts.googleapis.com/css2?family=Cinzel:wght@400&family=Sorts+Mill+Goudy&display=swap" rel="stylesheet">
<style>
  :root {
    --night: #040303;
    --ember-core: #fffbe6;
    --ember-hot: #ffd24a;
    --ember-flame: #f39a1e;
    --ember-glow: #c9601c;
    --ember-rust: #7a3612;
    --floor-warm: #5a3418;
    --floor-cold: #1b2119;
    --title-red: #a81f2e;
    --name-white: #f6f3ec;
  }
  html, body {
    margin: 0;
    padding: 0;
    width: 1200px;
    height: 1200px;
    overflow: hidden;
    background: var(--night);
  }
  .album-cover {
    position: relative;
    width: 1200px;
    height: 1200px;
    overflow: hidden;
    background: var(--night);
  }
  .cover-photo {
    position: absolute;
    inset: 0;
    background:
      radial-gradient(ellipse 110px 150px at 640px 470px, var(--ember-core) 0%, rgba(255,240,190,0.9) 45%, rgba(255,210,74,0) 100%),
      radial-gradient(ellipse 130px 220px at 620px 380px, rgba(255,220,120,0.95) 0%, rgba(243,154,30,0.8) 50%, rgba(243,154,30,0) 100%),
      radial-gradient(ellipse 80px 90px at 760px 560px, rgba(255,230,150,0.9) 0%, rgba(243,154,30,0) 100%),
      radial-gradient(ellipse 200px 140px at 820px 400px, rgba(230,130,50,0.7) 0%, rgba(201,96,28,0) 100%),
      radial-gradient(ellipse 300px 330px at 660px 480px, rgba(201,96,28,0.75) 0%, rgba(122,54,18,0.35) 60%, rgba(122,54,18,0) 100%),
      radial-gradient(ellipse 420px 300px at 1000px 650px, rgba(150,80,30,0.75) 0%, rgba(90,52,24,0.45) 55%, rgba(90,52,24,0) 100%),
      radial-gradient(ellipse 360px 260px at 300px 620px, rgba(90,52,24,0.6) 0%, rgba(60,36,20,0.3) 55%, rgba(40,26,16,0) 100%),
      radial-gradient(ellipse 260px 160px at 620px 760px, rgba(40,18,8,0.85) 0%, rgba(40,18,8,0) 100%),
      radial-gradient(ellipse 240px 260px at 880px 1000px, rgba(8,6,4,0.9) 0%, rgba(8,6,4,0) 100%),
      linear-gradient(180deg, #020101 0%, #050302 28%, #2a1a0f 48%, #3a2616 62%, #1f1d14 80%, #121612 100%);
  }
  .cover-credits {
    position: absolute;
    left: 48px;
    bottom: 28px;
  }
  .artist-name {
    margin: 0;
    font-family: "Sorts Mill Goudy", "Goudy Old Style", serif;
    font-weight: 400;
    font-size: 54px;
    line-height: 1;
    letter-spacing: 1px;
    color: var(--name-white);
  }
  .album-title {
    margin: 10px 0 0 0;
    font-family: "Cinzel", "Trajan Pro", serif;
    font-weight: 400;
    font-size: 126px;
    line-height: 1;
    letter-spacing: -2px;
    color: var(--title-red);
  }
</style>
</head>
<body>
  <main class="album-cover">
    <div class="cover-photo" role="img" aria-label="Night photograph of a segmented metal figure lying face down on paving stones, its torso engulfed in bright flames, with scrap metal frames, an overturned chair and cables around it"></div>
    <div class="cover-credits">
      <p class="artist-name">Lucien Marrow</p>
      <h1 class="album-title">OSTRA</h1>
    </div>
  </main>
</body>
</html>
```